Brightleaf Homes needs a web design and brand identifier

Brightleaf Homes is a pioneering approach by local councils and four greenhouse alliances to support low income households to install solar systems with no upfront costs.

Brightleaf Homes will commence in May 2017.

Brightleaf Homes is looking for a designer to create a website banner incorporating a brand identifier for Brightleaf Homes. The brand identifier will be used in Brightleaf Homes promotional materials, such as flyers and mail outs.

The website banner and brand identifier should engender trust and confidence in the target group (retirees).
Updates

Project Deadline Extended
Reason: Hi, Thank you for your work so far. We've been given advice to get a separate logo designed (instead of trying to include this as part of the banner design). Sorry for not realising this until now - we're new to all this. So, I have a couple of preliminary logo designs that are being considered by our project control group. I will forward a copy of the logo once we have it. The project control group is looking for a web design that is unique to Brightleaf Homes and a design that draws on the key elements of the program (i.e. it helps people save money and take control). The site should be friendly but not too informal as the target group is seniors. Here's a link to another community energy organisation: www.kelvowattgroup.com.au/ Apologies again for the delays. Cheers, Tomas

Target Market(s)

Home owning, low income, retirees

Industry/Entity Type

Non Profit

Number of Pages Required

1 page

Font styles to use
Sans Serif

Requirements
Must have
• Use of Brightleaf Home name
• Must promote Brightleaf Homes as safe, reliable and trustworthy
Nice to have
• Blue - to engender sense of safety and confidence (open to suggestions, though)
• Solar panels / the sun
Should not have
• Anything that is hard to read
• anything that promotes riskyness

```html
<!DOCTYPE html>
<html lang="en">
<head>
<meta charset="utf-8">
<title>Brightleaf Homes</title>
<link rel="stylesheet" href="https://fonts.googleapis.com/css2?family=Titillium+Web:wght@400;600;700&family=Open+Sans:wght@400;600;700&display=swap">
<style>
:root{
  --blue:#3a8fd6;
  --blue-deep:#2c7cc4;
  --navy:#2b3a4d;
  --red:#e84c3d;
  --sand:#e6d69a;
  --sand-deep:#d8c276;
  --orange:#f4a61d;
  --text:#3c3c3c;
  --muted:#6b6b6b;
  --light:#eceef0;
  --white:#ffffff;
}
*{box-sizing:border-box;margin:0;padding:0}
html,body{width:1200px;height:3158px;overflow:hidden}
body{font-family:"Open Sans",Arial,sans-serif;color:var(--text);background:var(--white);position:relative}
h1,h2,h3,.brand,.nav a,.btn{font-family:"Titillium Web",Arial,sans-serif}
.abs{position:absolute}

/* header */
.site-header{position:absolute;top:0;left:0;width:1200px;height:72px;background:var(--white)}
.brand{position:absolute;left:173px;top:16px;font-size:28px;font-weight:600;color:var(--blue);white-space:nowrap}
.nav{position:absolute;left:430px;top:27px;display:flex;gap:32px}
.nav a{font-size:13px;color:var(--navy);text-decoration:none;text-transform:uppercase;letter-spacing:.3px;white-space:nowrap}
.btn-quote{position:absolute;left:890px;top:22px;width:138px;height:29px;border-radius:15px;background:var(--red);color:var(--white);font-size:12px;font-weight:700;text-align:center;line-height:29px;text-transform:uppercase}

/* hero */
.hero{position:absolute;top:72px;left:0;width:1200px;height:503px;overflow:hidden}
.hero-photo{position:absolute;inset:0;background:linear-gradient(90deg,#4a4540 0%,#7e7468 38%,#c4b6a5 62%,#d8cdbf 80%,#b8aea2 100%)}
.hero-copy{position:absolute;left:170px;top:140px;width:420px;color:var(--white)}
.hero-kicker{font-family:"Titillium Web",sans-serif;font-size:24px;font-weight:400;text-transform:uppercase;line-height:1}
.hero-title{font-size:50px;font-weight:700;text-transform:uppercase;line-height:1.1;margin-top:6px;padding-bottom:8px;border-bottom:1px solid rgba(255,255,255,.7);width:410px}
.hero-text{font-size:17px;line-height:1.6;margin-top:30px;width:400px}
.hero-phone{display:flex;align-items:center;gap:14px;margin-top:22px;font-size:25px}

/* welcome */
.section-title{font-size:33px;font-weight:700;color:#1d1d1d;text-transform:uppercase;text-align:center}
.rule{width:44px;height:3px;background:var(--blue);margin:10px auto 0}
.welcome{position:absolute;top:630px;left:0;width:1200px}
.video{position:absolute;left:173px;top:90px;width:425px;height:240px;background:linear-gradient(180deg,#8fb4a8 0%,#7aa394 45%,#5f8c70 70%,#4f7a5b 100%)}
.video-play{position:absolute;left:180px;top:80px}
.video-label{position:absolute;left:0;width:100%;top:160px;text-align:center;color:var(--white);font-size:12px;font-weight:700;text-transform:uppercase}
.welcome-text{position:absolute;left:632px;top:98px;width:352px;font-size:15px;line-height:1.55;color:var(--text)}
.welcome-text p+p{margin-top:22px}

/* how it works */
.how{position:absolute;top:1031px;left:0;width:1200px;height:480px;background:var(--sand);overflow:hidden}
.how-scene{position:absolute;left:0;bottom:0;width:1200px;height:190px;background:linear-gradient(180deg,rgba(216,194,118,0) 0%,#c9ad5a 45%,#3f7fc0 75%,#2e6aa8 100%)}
.how .section-title{position:absolute;top:40px;width:100%;font-size:26px}
.how .rule{position:absolute;top:82px;left:578px;margin:0}
.steps{position:absolute;top:116px;left:177px;display:flex;gap:27px}
.step{position:relative;width:191px;height:291px;background:var(--white);border-radius:5px;box-shadow:0 2px 6px rgba(0,0,0,.12);text-align:center}
.step-num{position:absolute;left:-8px;top:-10px;width:32px;height:32px;border-radius:50%;background:var(--red);color:var(--white);font-family:"Titillium Web",sans-serif;font-weight:700;font-size:15px;line-height:32px}
.step-icon{width:126px;height:126px;border-radius:50%;margin:28px auto 0;background:radial-gradient(circle at 45% 40%,#ffd24a 0%,#f7b52a 55%,#ef9a1c 100%)}
.step p{font-size:12.5px;line-height:1.65;color:var(--muted);padding:28px 10px 0}

/* eligibility */
.eligible{position:absolute;top:1511px;left:0;width:1200px;height:527px}
.eligible h2{position:absolute;left:173px;top:268px;font-size:27px;font-weight:700;color:#1d1d1d;text-transform:uppercase}
.eligible .rule{position:absolute;left:173px;top:308px;margin:0;width:50px}
.eligible-note{position:absolute;left:173px;top:322px;font-size:13px;color:var(--muted)}
.bubble{position:absolute;border-radius:50%;display:flex;align-items:center;justify-content:center;text-align:center;color:var(--white);font-size:13px;font-weight:700;line-height:1.3}
.b-owner{left:532px;top:179px;width:144px;height:144px;background:var(--navy)}
.b-pension{left:678px;top:83px;width:210px;height:210px;background:var(--blue)}
.b-home{left:638px;top:300px;width:168px;height:168px;background:var(--blue-deep)}
.b-usage{left:825px;top:251px;width:202px;height:202px;background:var(--red)}

/* who */
.who{position:absolute;top:2038px;left:0;width:1200px;height:452px;overflow:hidden}
.who-photo{position:absolute;inset:0;background:linear-gradient(160deg,#1f7fd4 0%,#4aa3e6 35%,#2a5d9a 60%,#c9552a 80%,#e9e3d8 100%)}
.who h2{position:absolute;left:173px;top:42px;font-size:40px;font-weight:700;color:var(--white);text-transform:uppercase}
.who .rule{position:absolute;left:173px;top:96px;margin:0;background:var(--white);width:50px}
.who p{position:absolute;left:173px;top:108px;width:345px;font-size:13px;line-height:1.6;color:var(--white)}

/* what next */
.next{position:absolute;top:2490px;left:0;width:1200px;height:173px;background:var(--red);color:var(--white);text-align:center}
.next h2{font-size:28px;font-weight:700;text-transform:uppercase;margin-top:30px}
.next .rule{background:var(--white);width:50px;margin-top:6px}
.next p{font-size:14px;margin-top:18px}
.next .contact{font-size:18px;font-weight:700;margin-top:6px}
.next .contact span{font-weight:400;font-size:14px;margin:0 8px}

/* partners */
.partners{position:absolute;top:2663px;left:0;width:1200px;height:227px;background:var(--light)}
.partners h3{font-size:17px;font-weight:700;color:#1d1d1d;text-transform:uppercase;text-align:center;margin-top:44px}
.partners .rule{width:44px;margin-top:8px}
.partner-row{position:absolute;top:100px;left:230px;display:flex;gap:110px;align-items:center}
.badge{width:150px;height:60px;border-radius:4px}
.badge-a{width:120px;height:78px;border-radius:50%;background:#7db041}
.badge-b{background:#8a8f96}
.badge-c{background:#97c23c}
.badge-d{width:110px;height:70px;border-radius:50%;background:#2aa3c9}

/* footer */
.site-footer{position:absolute;top:2890px;left:0;width:1200px;height:268px;background:var(--navy);color:#c7ced6;font-size:11.5px}
.fcol{position:absolute;top:30px}
.fcol h4{font-family:"Open Sans",sans-serif;font-size:12px;font-weight:700;color:var(--white);text-transform:uppercase;margin-bottom:16px}
.fcol li{list-style:none;line-height:24px}
.fcol .item{display:flex;gap:10px;margin-bottom:10px;line-height:1.5}
.social{display:flex;gap:12px}
.social span{width:20px;height:20px;border:2px solid #c7ced6;border-radius:50%}
.field{width:200px;height:32px;background:#43536a;color:var(--white);padding-left:10px;line-height:32px;margin-bottom:8px}
.join{width:200px;height:32px;background:var(--blue);color:var(--white);text-align:center;line-height:32px;font-weight:700;text-transform:uppercase}
.copyright{position:absolute;left:173px;top:248px;font-size:10.5px;color:#c7ced6}
</style>
</head>
<body>

<header class="site-header">
  <div class="brand">Brightleaf Homes</div>
  <nav class="nav">
    <a>Home</a><a>About Us</a><a>Services</a><a>How It Works</a><a>Contact Us</a>
  </nav>
  <div class="btn-quote btn">Request a Quote</div>
</header>

<section class="hero">
  <div class="hero-photo" role="img" aria-label="Photo of a smiling elderly couple at home, warm soft light"></div>
  <div class="hero-copy">
    <div class="hero-kicker">Help pensioner households to</div>
    <h1 class="hero-title">Save Money</h1>
    <p class="hero-text">and take control of their energy bills by installing an affordable, quality solar system and be part of an Australian first</p>
    <div class="hero-phone">
      <svg width="26" height="26" viewBox="0 0 24 24" fill="none" stroke="#fff" stroke-width="1.6"><path d="M5 3h4l2 5-2.5 1.5a11 11 0 0 0 6 6L16 13l5 2v4a2 2 0 0 1-2 2A17 17 0 0 1 3 5a2 2 0 0 1 2-2z"/></svg>
      <span>0400 555 218</span>
    </div>
  </div>
</section>

<section class="welcome">
  <h2 class="section-title">Welcome to Brightleaf Homes</h2>
  <div class="rule"></div>
  <div class="video" role="img" aria-label="Video still: illustration of a house with solar panels and wind turbines among green hills">
    <svg class="video-play" width="66" height="66" viewBox="0 0 66 66"><circle cx="33" cy="33" r="30" fill="none" stroke="#fff" stroke-width="3"/><path d="M26 20l22 13-22 13z" fill="#fff"/></svg>
    <div class="video-label">Watch Video</div>
  </div>
  <div class="welcome-text">
    <p>We need you Help pensioner households to save money and take control of their energy bills by installing anaffordable, quality solar system and be part of an Australian first.</p>
    <p>Brightleaf Homes is a pioneering approach by local councils to support pensioner households to install solar with no upfront costs. We’ve done the hard work of finding a safe, reliable and quality installer so pensioners don’t have to.</p>
  </div>
</section>

<section class="how">
  <svg class="abs" style="left:0;top:0" width="1200" height="40" viewBox="0 0 1200 40" preserveAspectRatio="none"><path d="M0 0H1200V18C1000 40 820 4 600 20S200 36 0 14Z" fill="#fff"/></svg>
  <div class="how-scene" role="img" aria-label="Illustration of a city skyline with rows of solar panels in the foreground"></div>
  <h2 class="section-title">How It Works</h2>
  <div class="rule"></div>
  <div class="steps">
    <div class="step"><div class="step-num">01</div><div class="step-icon" role="img" aria-label="Icon of a sun with a plug"></div><p>Brightleaf Homes checks that every person gets a solar system that pays for itself in energy savings from day one</p></div>
    <div class="step"><div class="step-num">02</div><div class="step-icon" role="img" aria-label="Icon of a solar panel with a battery"></div><p>Brightleaf Homes organises for the solar system to be installed</p></div>
    <div class="step"><div class="step-num">03</div><div class="step-icon" role="img" aria-label="Icon of a supportive advisor"></div><p>Brightleaf Homes supports pensioners to understand and get the most out of solar</p></div>
    <div class="step"><div class="step-num">04</div><div class="step-icon" role="img" aria-label="Icon of a solar panel with zero percent interest"></div><p>Pensioners gradually pay for cost through their usual rates payments at 0% interest</p></div>
  </div>
</section>

<section class="eligible">
  <h2>Is my client eligible?</h2>
  <div class="rule"></div>
  <p class="eligible-note">Refer clients who are:</p>
  <div class="bubble b-pension">Pension Card Holders</div>
  <div class="bubble b-owner">Homeowners</div>
  <div class="bubble b-usage">Average to High<br>Electricity Users</div>
  <div class="bubble b-home">Usually At Home<br>From 9am to 5pm</div>
</section>

<section class="who">
  <div class="who-photo" role="img" aria-label="Photo of solar panels on a terracotta tiled roof under a bright blue sky"></div>
  <h2>Who is Brightleaf Homes?</h2>
  <div class="rule"></div>
  <p>Over 20 local councils have come together with support from the State Government's Clean Power Futures Fund to run the Brightleaf Home program.</p>
</section>

<section class="next">
  <h2>What Next?</h2>
  <div class="rule"></div>
  <p>To refer clients or for further information, contact Tomas Hollis at Brightleaf Homes:</p>
  <div class="contact">0400 555 218<span>or</span>tomas.hollis@brightleafhomes.org.au</div>
</section>

<section class="partners">
  <h3>Brightleaf Homes is a partnership between</h3>
  <div class="rule"></div>
  <div class="partner-row">
    <div class="badge badge-a" role="img" aria-label="Partner greenhouse alliance"></div>
    <div class="badge badge-b" role="img" aria-label="Partner greenhouse alliance"></div>
    <div class="badge badge-c" role="img" aria-label="Partner greenhouse alliance"></div>
    <div class="badge badge-d" role="img" aria-label="Partner climate change alliance"></div>
  </div>
</section>

<footer class="site-footer">
  <div class="fcol" style="left:173px"><h4>Quick Links</h4><ul><li>Home</li><li>About Us</li><li>Services</li><li>How It Works</li><li>Contact Us</li></ul></div>
  <div class="fcol" style="left:296px"><h4>Support</h4><ul><li>Contact us</li><li>FAQs</li><li>Legal</li><li>Privacy Policy</li><li>Legal</li></ul></div>
  <div class="fcol" style="left:415px">
    <h4>Contact Us</h4>
    <div class="item"><svg width="12" height="14" viewBox="0 0 12 14" fill="none" stroke="#c7ced6" stroke-width="1.3"><path d="M6 13s5-5 5-8A5 5 0 0 0 1 5c0 3 5 8 5 8z"/><circle cx="6" cy="5" r="1.8"/></svg><span>Your Company LTD.<br>Street Name, 000000<br>City Name</span></div>
    <div class="item"><svg width="12" height="12" viewBox="0 0 24 24" fill="none" stroke="#c7ced6" stroke-width="2"><path d="M5 3h4l2 5-2.5 1.5a11 11 0 0 0 6 6L16 13l5 2v4a2 2 0 0 1-2 2A17 17 0 0 1 3 5a2 2 0 0 1 2-2z"/></svg><span>Phone<br>0400 555 218</span></div>
    <div class="item"><svg width="12" height="10" viewBox="0 0 12 10" fill="none" stroke="#c7ced6" stroke-width="1.2"><rect x=".6" y=".6" width="10.8" height="8.8"/><path d="M.6.6L6 5l5.4-4.4"/></svg><span>Email<br>tomas.hollis@brightleafhomes.org.au</span></div>
  </div>
  <div class="fcol" style="left:646px"><h4>Get Connected</h4><div class="social" aria-hidden="true"><span></span><span></span><span></span><span></span></div></div>
  <div class="fcol" style="left:830px"><h4>E-Newsletter Signup</h4><div class="field">Name</div><div class="field">Email</div><div class="join">Join</div></div>
  <div class="copyright">© 2017 Brightleaf Homes. All Rights Reserved</div>
</footer>

</body>
</html>
```